Einladungskarten
Zielgruppe
Wir sind die Gewerbeverbund Talbrück-Moos. Eine Organisation zur Interessenvertretung, Beratung und Unterstützung von Handwerksbetrieben. Unsere Zielgruppe sind Handwerksbetriebe.
Aufgabenstellung
Das Design soll modern sein. Es handelt sich um Einladungskarten zu einer Veranstaltung, die per Post verschickt werden sollen. Format: DIN Lang.
Die Veranstaltung hat den Titel: Brot, Käse und Chips
Einlass: 18:00 Uhr
Beginn: 18:30 Uhr
Adresse: Kickwiese Olmen - Lerchenweg 14, 41876 Olmen
Veranstalter: GVA vital und Gewerbeverbund Talbrück-Moos

```html
<!DOCTYPE html>
<html lang="de">
<head>
<meta charset="utf-8">
<title>Einladung – Brot, Käse und Chips</title>
<link href="https://fonts.googleapis.com/css2?family=Arimo:wght@400;700&display=swap" rel="stylesheet">
<style>
  :root {
    --brand-blue: #2f4e9b;
    --white: #ffffff;
    --orange: #e8622f;
    --red: #b8273f;
    --teal: #25b4cf;
    --sky: #1a9ad8;
    --purple: #46237f;
    --violet: #5a2f8c;
    --pink: #b673ad;
    --peach: #eea878;
  }
  * { box-sizing: border-box; margin: 0; padding: 0; }
  html, body { width: 1172px; height: 1200px; overflow: hidden; background: var(--white); }
  body { font-family: "Arimo", Arial, sans-serif; color: var(--brand-blue); position: relative; }

  .card { position: absolute; left: 0; width: 1172px; height: 586px; overflow: hidden; }
  .card--front { top: 0; }
  .card--back { top: 614px; }

  .card__pattern { position: absolute; inset: 0; }
  .card--front .card__pattern {
    background:
      radial-gradient(ellipse 340px 300px at 60px 380px, var(--orange), transparent 75%),
      radial-gradient(ellipse 300px 240px at 120px 560px, var(--red), transparent 80%),
      radial-gradient(ellipse 420px 200px at 380px 40px, var(--teal), transparent 75%),
      radial-gradient(ellipse 260px 200px at 600px 190px, var(--peach), transparent 75%),
      radial-gradient(ellipse 300px 300px at 1100px 320px, var(--sky), transparent 75%),
      radial-gradient(ellipse 400px 120px at 560px 580px, var(--pink), transparent 80%),
      linear-gradient(110deg, var(--violet), var(--purple) 60%, #3a2a86);
  }
  .card--back .card__pattern {
    background:
      radial-gradient(ellipse 300px 380px at 20px 470px, var(--peach), transparent 75%),
      radial-gradient(ellipse 500px 140px at 650px 590px, var(--teal), transparent 75%),
      radial-gradient(ellipse 220px 300px at 1160px 440px, var(--sky), transparent 75%),
      radial-gradient(ellipse 200px 200px at 20px 120px, #3b8cc0, transparent 75%),
      linear-gradient(180deg, var(--purple), #3d2f80 60%, #3e4f98);
  }

  .front__frame {
    position: absolute; left: 56px; top: 56px; width: 1060px; height: 470px;
    border: 4px solid var(--white); border-radius: 3px;
  }
  .front__partners {
    position: absolute; left: 907px; top: 56px; width: 209px; height: 175px;
    background: var(--white); border-radius: 4px;
    display: flex; flex-direction: column; justify-content: center; gap: 26px;
    padding: 0 22px 0 40px;
  }
  .partner { display: flex; align-items: center; gap: 8px; font-weight: 700; color: var(--brand-blue); }
  .partner--main { font-size: 24px; }
  .partner--guild { font-size: 9px; line-height: 1.25; }
  .partner__dot { width: 14px; height: 14px; border-radius: 50%; background: var(--brand-blue); flex: none; }
  .partner__square { width: 30px; height: 30px; background: var(--brand-blue); flex: none; }

  .front__heading {
    position: absolute; left: 0; width: 1190px; top: 166px; text-align: center;
    color: var(--white); font-weight: 400; font-size: 74px; line-height: 1;
  }
  .front__title {
    position: absolute; left: 203px; top: 283px; width: 765px; height: 240px;
    background: var(--white); border-radius: 5px;
    display: flex; flex-direction: column; align-items: center; justify-content: center;
    font-weight: 700; text-transform: uppercase; line-height: 0.92;
    padding-top: 8px;
  }
  .front__title .title__top { font-size: 77px; }
  .front__title .title__bottom { font-size: 110px; }

  .back__panel {
    position: absolute; left: 56px; top: 61px; width: 1060px; height: 469px;
    background: var(--white); border-radius: 5px;
  }
  .back__title {
    position: absolute; left: 0; right: 0; top: 16px; text-align: center;
    font-weight: 700; text-transform: uppercase; line-height: 0.9;
  }
  .back__title .title__top { font-size: 51px; }
  .back__title .title__bottom { font-size: 84px; }
  .back__intro {
    position: absolute; left: 147px; top: 149px; font-size: 23px; white-space: nowrap;
  }
  .info-box {
    position: absolute; top: 198px; width: 368px; height: 200px;
    border: 4px solid var(--brand-blue); border-radius: 3px;
    font-size: 31px; line-height: 38px; font-style: normal;
  }
  .info-box--time { left: 147px; padding: 16px 0 0 21px; }
  .info-box--venue { left: 547px; padding: 10px 0 0 18px; }
  .info-box dt, .info-box .info-box__label { font-weight: 700; }
  .info-box dd { margin: 0; }
  .back__organizer {
    position: absolute; left: 0; right: 0; top: 423px; text-align: center; font-size: 23px;
  }
</style>
</head>
<body>
  <section class="card card--front">
    <div class="card__pattern" role="img" aria-label="Farbiges Low-Poly-Dreiecksmuster in Orange, Rot, Türkis und Violett"></div>
    <div class="front__frame"></div>
    <div class="front__partners">
      <div class="partner partner--main"><span class="partner__dot"></span>GVA vital</div>
      <div class="partner partner--guild"><span class="partner__square"></span>Gewerbeverbund<br>Talbrück-Moos</div>
    </div>
    <h1 class="front__heading">Einladung</h1>
    <div class="front__title">
      <span class="title__top">Brot, Käse</span>
      <span class="title__bottom">und Chips</span>
    </div>
  </section>

  <section class="card card--back">
    <div class="card__pattern" role="img" aria-label="Farbiges Low-Poly-Dreiecksmuster in Violett, Blau, Türkis und Pfirsich"></div>
    <div class="back__panel">
      <h2 class="back__title">
        <span class="title__top">Brot, Käse</span><br>
        <span class="title__bottom">und Chips</span>
      </h2>
      <p class="back__intro">Sie sind herzlich zu unserer Veranstaltung „Brot, Käse und Chips“ eingeladen.</p>
      <dl class="info-box info-box--time">
        <dt>Einlass</dt><dd>18:00 Uhr</dd>
        <dt>Beginn</dt><dd>18:30 Uhr</dd>
      </dl>
      <address class="info-box info-box--venue">
        <span class="info-box__label">Veranstaltungsort</span><br>
        Kickwiese Olmen<br>
        Lerchenweg 14<br>
        41876 Olmen
      </address>
      <p class="back__organizer">Veranstalter: GVA vital und Gewerbeverbund Talbrück-Moos</p>
    </div>
  </section>
</body>
</html>
```